Slider needed for Database Documentation Topic

We need a slider to promote a content area of a web site. I'm listing this as a poster because the posters I have seen on Quillbarn portfolios most closely resemble the combination or art and text I am looking for.
The content area we are promoting with this graphic will clarify the design and use of a complicated database. The title of the content area is "The Marbled QZ Database" and the banner should use that title.
To 'illuminate' something means to cast light on it, and this content area will help shed light on a complicated thing – the content will use diagrams, text, and examples to clarify the database. Another meaning is that an illuminated manuscript is a manuscript brought to life with pictures, and in a way that is also what this content area will do.
One idea for the slider might be a light bulb, lamp, candle or flashlight lighting up the words "QZ Database". Another idea would be the type of illustration you see if you search for "Illuminated manuscript"
But I'm not committed to any particular idea - in the past I have been pleased to see ideas that are different than my own but accomplish the same thing, so please feel free to use your judgement or ask any questions.
In addition to the title (The Marbled QZ Database) the graphic should allow room for three smaller lines of text – the three bullet items below:
- Guide to understanding the QZ database
- Data sources, uses and relationships explained with illustrations
- New content! Customers
The last bullet item will change as the content is added.
Some particulars ...
SIZE - 600 high x 1200 wide pixels
PHOTOS vs ILLUSTRATION - I am open to either one.

```html
<!DOCTYPE html>
<html lang="en">
<head>
<meta charset="utf-8">
<title>The Marbled QZ Database</title>
<link rel="stylesheet" href="https://fonts.googleapis.com/css2?family=Roboto+Condensed:wght@300;400;700&display=swap">
<style>
  :root {
    --deep-blue: #0a2a8c;
    --royal-blue: #1546c8;
    --glow-blue: #4d8cff;
    --cyan: #36d2ff;
    --ice: #cdeeff;
    --ribbon: #a9e6fb;
    --ink: #0b1433;
    --white: #ffffff;
    --frame: rgba(210, 230, 255, 0.85);
  }
  * { margin: 0; padding: 0; box-sizing: border-box; }
  html, body { width: 1200px; height: 600px; overflow: hidden; background: var(--deep-blue); }
  .slider {
    position: relative;
    width: 1200px;
    height: 600px;
    overflow: hidden;
    font-family: "Roboto Condensed", "Arial Narrow", sans-serif;
  }
  .backdrop {
    position: absolute; inset: 0;
    background:
      radial-gradient(ellipse 520px 340px at 620px 230px, rgba(120,170,255,0.55), transparent 70%),
      linear-gradient(160deg, #0d3aa8 0%, var(--royal-blue) 45%, #0a2f9e 75%, #071f78 100%);
  }
  .bulb-glow {
    position: absolute;
    left: 555px; top: 0;
    width: 200px; height: 200px;
    border-radius: 0 0 50% 50%;
    background: radial-gradient(circle at 50% 62%, #ffffff 0%, #cfe4ff 22%, rgba(110,160,255,0.6) 55%, transparent 72%);
  }
  .frame {
    position: absolute; inset: 0;
  }
  .ribbon {
    position: absolute;
    left: 265px; top: 219px;
    width: 300px; height: 38px;
    background: var(--ribbon);
    clip-path: polygon(0 0, 91% 0, 100% 50%, 91% 100%, 0 100%);
    color: var(--ink);
    font-size: 31px;
    line-height: 38px;
    padding-left: 32px;
    letter-spacing: 0.5px;
    text-transform: uppercase;
  }
  .ribbon .light { font-weight: 300; }
  .ribbon .strong { font-weight: 700; }
  .title {
    position: absolute;
    left: 574px; top: 190px;
    font-size: 82px;
    font-weight: 300;
    color: var(--ice);
    letter-spacing: -1px;
    line-height: 1;
    text-shadow: 0 0 18px rgba(120,200,255,0.5);
  }
  .points {
    position: absolute;
    left: 312px; top: 262px;
    list-style: none;
    color: var(--white);
    font-size: 29px;
    line-height: 34px;
  }
  .points li {
    position: relative;
    padding-left: 34px;
    margin-bottom: 5px;
  }
  .points li::before {
    content: "•";
    position: absolute;
    left: 0; top: 0;
    color: var(--ice);
  }
  .points .accent { color: var(--cyan); font-weight: 700; }
  .doc-icon {
    position: absolute;
    left: 788px; top: 318px;
    width: 125px; height: 155px;
  }
</style>
</head>
<body>
<main class="slider">
  <div class="backdrop" role="img" aria-label="Deep blue background with softly curving rows of glowing binary digits"></div>
  <div class="bulb-glow" role="img" aria-label="Glowing light bulb hanging from the top, casting light on the title"></div>

  <svg class="frame" width="1200" height="600" viewBox="0 0 1200 600" aria-hidden="true">
    <g fill="none" stroke="var(--frame)" stroke-width="1.2">
      <polyline points="265,238 240,238 240,410 790,410"/>
      <polyline points="930,238 965,238 965,410 905,410"/>
    </g>
  </svg>

  <div class="ribbon"><span class="light">The </span><span class="strong">Marbled</span></div>
  <h1 class="title">QZ Database</h1>

  <ul class="points">
    <li><span class="accent">Guide to</span> understanding the <span class="accent">QZ database</span></li>
    <li><span class="accent">Data Sources,</span> Uses and Relationships<br>explained with illustrations</li>
    <li><span class="accent">New content!</span> Customers</li>
  </ul>

  <svg class="doc-icon" viewBox="0 0 125 155" aria-hidden="true">
    <defs>
      <linearGradient id="iconStroke" x1="0" y1="0" x2="1" y2="1">
        <stop offset="0" stop-color="#7fe6ff"/>
        <stop offset="1" stop-color="#2fb6ff"/>
      </linearGradient>
    </defs>
    <g fill="none" stroke="url(#iconStroke)" stroke-width="5" stroke-linecap="round" stroke-linejoin="round">
      <rect x="30" y="4" width="62" height="82" rx="10" fill="rgba(20,60,170,0.55)"/>
      <rect x="4" y="22" width="72" height="94" rx="10" fill="rgba(20,60,170,0.75)"/>
      <line x1="18" y1="46" x2="58" y2="46"/>
      <line x1="18" y1="62" x2="46" y2="62"/>
      <line x1="18" y1="78" x2="40" y2="78"/>
      <line x1="18" y1="94" x2="36" y2="94"/>
      <circle cx="80" cy="88" r="28" fill="rgba(20,60,170,0.85)"/>
      <polyline points="67,88 77,98 94,78"/>
      <line x1="100" y1="110" x2="116" y2="138" stroke-width="10"/>
    </g>
  </svg>
</main>
</body>
</html>
```